Valtrona Corporate Stationery

Look for design of all new corporate stationery for an existing insurance broking business that is going through a redesign and move from older partners to younger family members. New Logo is attached. Company is Brisbane based.
Colours in the Logo is Hex #43bed8 and website features a lot of hex #17b8d8. Website front page "A plan to protect you" - headline. "Professional and Individual advice to protect your greatest assets" - tagline.

Stationery required: Business Cards, Letter head, Thank-you cards, Birthday cards, Presentation folders, With Compliment slips and a powerpoint template. We also would like to send a card to all customers with the something along of the lines of "something new".

Target Market(s)

Customers of Insurance business looking at superannuation, life and income protection insurance, investment advice and wills

Industry/Entity Type

Insurance Broker

Font styles to use
Other font styles liked:
• same as logo

Requirements
Must have
• The above designs for new stationery for the new business including:
• Business Cards, Letter head, Thank-you cards, Birthday cards, Presentation folders, With Compliment slips and a powerpoint template. We also would like to send a card to all customers with the something along of the lines of "something new".
Nice to have
• It is a new look - long time family business being passed to next generation - big focus on advice for YOU, individual advice etc..

```html
<!DOCTYPE html>
<html lang="en">
<head>
<meta charset="utf-8">
<title>Valtrona Financial Group — Business Cards</title>
<link href="https://fonts.googleapis.com/css2?family=Montserrat:wght@300;400;500;600&display=swap" rel="stylesheet">
<style>
  :root {
    --brand-cyan: #43bed8;
    --brand-cyan-deep: #17b8d8;
    --ink-grey: #6d6e71;
    --paper: #ffffff;
    --backdrop: #ece8e2;
    --card-shadow: rgba(40, 30, 20, 0.25);
  }
  * { box-sizing: border-box; margin: 0; padding: 0; }
  html, body {
    width: 1200px; height: 950px; overflow: hidden;
    background: var(--backdrop);
    font-family: "Montserrat", Arial, sans-serif;
  }
  .canvas { position: relative; width: 1200px; height: 950px; }

  .card {
    position: absolute;
    width: 600px; height: 340px;
    border-radius: 4px;
    box-shadow: 0 14px 30px var(--card-shadow);
    overflow: hidden;
  }

  /* Back of card: contact details */
  .card-back {
    left: 90px; top: 90px;
    background: linear-gradient(160deg, var(--brand-cyan) 0%, var(--brand-cyan-deep) 100%);
    color: var(--paper);
  }
  .contact-block {
    position: absolute; left: 44px; bottom: 40px;
    font-weight: 400; font-size: 17px; line-height: 1.35; letter-spacing: 0.3px;
  }
  .address { margin-bottom: 12px; }
  .contact-list { list-style: none; }
  .contact-list li { display: flex; align-items: center; gap: 10px; }
  .contact-list svg { width: 14px; height: 14px; flex: none; fill: var(--paper); }

  /* Front of card: name and company */
  .card-front {
    left: 520px; top: 530px;
    background: var(--paper);
  }
  .company {
    position: absolute; left: 70px; top: 100px;
    display: flex; align-items: center; gap: 18px;
  }
  .company-dot {
    width: 46px; height: 46px; border-radius: 50%;
    background: var(--brand-cyan);
  }
  .company-name {
    font-weight: 500; font-size: 34px; letter-spacing: 1.5px;
    color: var(--brand-cyan); text-transform: uppercase; line-height: 1;
  }
  .person {
    position: absolute; left: 70px; top: 210px;
    font-size: 17px; letter-spacing: 1.5px; text-transform: uppercase;
  }
  .person-name { color: var(--brand-cyan); font-weight: 500; }
  .person-role { color: var(--ink-grey); font-weight: 400; }
</style>
</head>
<body>
<main class="canvas">

  <section class="card card-back" aria-label="Business card back">
    <div class="contact-block">
      <p class="address">214 Harbour Street<br>Brisbane, QLD 4000</p>
      <ul class="contact-list">
        <li>
          <svg viewBox="0 0 16 16" aria-hidden="true"><path d="M3.5 1l2.5 3-1.5 2c.8 1.8 2.2 3.2 4 4l2-1.5 3 2.5-1.5 2.5C6.5 13.5 2.5 9.5 1 3.5z"/></svg>
          <span>617 302 4481</span>
        </li>
        <li>
          <svg viewBox="0 0 16 16" aria-hidden="true"><path d="M4 1h8v14H4zM5.5 3v9h5V3z"/></svg>
          <span>617 845 2097</span>
        </li>
        <li>
          <svg viewBox="0 0 16 16" aria-hidden="true"><path d="M4 1h8v4H4zM1 6h14v7h-3v2H4v-2H1zm4 5v2h6v-2z"/></svg>
          <span>617 590 3362</span>
        </li>
        <li>
          <svg viewBox="0 0 16 16" aria-hidden="true"><path d="M1 3h14v10H1zm1.5 1.5L8 9l5.5-4.5z"/></svg>
          <span>hello@valtrona.example</span>
        </li>
        <li>
          <svg viewBox="0 0 16 16" aria-hidden="true"><circle cx="8" cy="8" r="7"/></svg>
          <span>www.valtrona.example</span>
        </li>
      </ul>
    </div>
  </section>

  <section class="card card-front" aria-label="Business card front">
    <div class="company">
      <span class="company-dot" aria-hidden="true"></span>
      <span class="company-name">Valtrona Financial Group</span>
    </div>
    <p class="person">
      <span class="person-name">Liam Carter</span>
      <span class="person-role"> - CEO/Founder</span>
    </p>
  </section>

</main>
</body>
</html>
```